Label Design for RTD Cocktail Line Tovelin Spirits

Tovelin Spirits is a line of Indian-inspired artisan cocktails that "brings the bartender home" for professional men and women who like the finer things in life but don’t always have the time to treat themselves. No need for a multitude of expensive and hard-to-find ingredients, time consuming recipes, or a mixologist.

Our line of 3 open and serve cocktails blends a range of premium spirits with exotic ingredients so you can conveniently raise a glass for any of life’s celebrations.

Our bottle is the 750ml Claret bottle with Quarnet (screw cap) closure and will be covered entirely in a shrink sleeve (so potentially anything can be designed for any part of the bottle). We want the bottle to pop on the shelf so it should look different than what’s already out there (Velvet Moth, Galdrova, Merlusa ready to drink cocktails). We are looking for a sexy design that's polished/sleek.
Updates

Project Deadline Extended
Reason: Hello designers! Tovelin Spirits is so impressed with what we have received thus far and we would like to give some of the designers a few extra days to make the edits we requested. It's never too late to submit! Thank you all!

Industry/Entity Type

It Professional

Requirements
Must have
• Front of bottle
* “Tovelin Spirits” name and Peacock Logo- but feel free to pull the elements apart and use them on the bottle in different ways
* Open & Serve
* 12% ALC/VOL
* 750 ml
* 3 different labels in a theme for
-Borvelle
-Faluntera
-Pomadrine

Borvelle Ideas- soft brown palate, the ingredients in chai spice (cloves, cardamom pods, nutmeg, black peppercorns, star anise, and cinnamon stick)

Faluntera Ideas -cool and refreshing, pale green shade (not clashing with logo), graphics of fresh mint leaves, green chili, lime, cucumber

Pomadrine Ideas- soft/pale pink shades, graphics of lychi fruit (outer red shell and inner pink flesh), ginger

Back of bottle
* explanation of the 3 cocktails
Borvelle: Forget what you think you know about chai, this is not the Queen’s tea-time drink! Borvelle is a smooth, sweetly -spiced cocktail made with vodka, black tea, and a combination of aromatic spices. This velvety cocktail is rich without being heavy. Enjoy chilled or over ice anytime.

Faluntera: Faluntera can’t make up its mind! This fusion of zesty lime, sweet mint, earthy cucumber and spicy chilies is so refreshing you’ll crave it on a hot summer day or a cool winter’s night. The exotic botanicals in gin add a complexity to the cocktail making this a refreshing but potent drink! Enjoy chilled or over ice anytime.

Pomadrine: East meet West. Delicate lychi meet hard-hitting whiskey. Pomadrine will tempt you senses with flavor, fragrance and beauty. The peppery kick of ginger and the intensity of the un-aged whiskey are softened by lychi’s intoxicating scent and subtle, sweet finish.

Please include
1. Bottled By QRW Spirits Company
2. Sample barcode (where you would place it in your design)
3. www.TovelinSpirits.example
4. GOVERNMENT WARNING: (1) According to the Surgeon General, women should not drink alcoholic beverages during pregnancy because of the risk of birth defects. (2) Consumption of alcoholic beverages impairs your ability to drive a car or operate machinery, and may cause health problems.

Optional to include
*"Bring the Bartender Home"
*"Tovelin Spirits” name and Peacock Logo on the back
*Entirely black sleeve with contrasting design

FYI the Fonts used in our logo are Geosans Light and Prakrta, but feel free to use other complimentary fonts on the other aspects.
Nice to have
• Optional to include

```html
<!DOCTYPE html>
<html lang="en">
<head>
<meta charset="utf-8">
<title>Tovelin Spirits – Cocktail Sleeve Line</title>
<link href="https://fonts.googleapis.com/css2?family=Josefin+Sans:wght@300;400&family=Parisienne&family=Oswald:wght@400;500&family=Lato:wght@400;700&display=swap" rel="stylesheet">
<style>
  :root {
    --page: #ffffff;
    --cap: #111111;
    --brand: #2fa6d6;
    --chai-sleeve: #e6e6e3;
    --chai-band: #6b6457;
    --chai-ink: #3d3a35;
    --chai-accent: #8a7b63;
    --chai-photo: #b48a5c;
    --mint-sleeve: #a9ead5;
    --mint-band: #5fdcb0;
    --mint-ink: #45c7a0;
    --mint-accent: #27a189;
    --mint-photo: #a4d47e;
    --pink-sleeve: #f5d3e8;
    --pink-band: #f257c0;
    --pink-ink: #e43db4;
    --pink-accent: #5a3d4e;
    --pink-photo: #e9c3c5;
    --body-ink: #3e3e3e;
  }
  * { box-sizing: border-box; margin: 0; padding: 0; }
  html, body { width: 1200px; height: 800px; overflow: hidden; background: var(--page); }
  .lineup { position: relative; width: 1200px; height: 800px; }

  .bottle { position: absolute; top: 155px; width: 146px; height: 570px; }
  .bottle svg.silhouette { position: absolute; inset: 0; }
  .neck-url {
    position: absolute; left: 48px; top: 10px; height: 72px;
    writing-mode: vertical-rl; transform: rotate(180deg);
    font: 400 5.5px "Lato", sans-serif; color: #fff; white-space: nowrap;
  }
  .sleeve { position: absolute; inset: 0; text-align: center; }

  .brand { position: absolute; top: 222px; left: 0; right: 0; }
  .brand-dot { display: block; width: 11px; height: 11px; border-radius: 50%; background: var(--brand); margin: 0 auto 4px; }
  .brand-name { font: 400 12px "Josefin Sans", sans-serif; color: var(--brand); letter-spacing: 0.4px; white-space: nowrap; }

  .product-name { position: absolute; top: 296px; left: 0; right: 0; font: 400 32px "Parisienne", cursive; line-height: 1; white-space: nowrap; }
  .back .product-name { font-size: 24px; top: 276px; }
  .tagline { position: absolute; top: 334px; left: 4px; right: 4px; font: 500 6.5px "Oswald", sans-serif; text-transform: uppercase; white-space: nowrap; }

  .photo { position: absolute; top: 352px; left: 13px; width: 120px; height: 78px; border-radius: 6px; }
  .volume { position: absolute; top: 455px; left: 24px; right: 24px; display: flex; justify-content: space-between; font: 400 5.5px "Lato", sans-serif; }
  .slogan { position: absolute; top: 472px; left: 0; right: 0; font: 500 7.5px "Oswald", sans-serif; text-transform: uppercase; letter-spacing: 0.5px; white-space: nowrap; }

  .story { position: absolute; top: 304px; left: 11px; right: 11px; padding: 5px 6px; border: 1px solid rgba(255,255,255,0.9); font: 400 5.9px/1.38 "Lato", sans-serif; text-align: justify; text-align-last: center; }
  .site { position: absolute; top: 418px; left: 0; right: 0; font: 400 5.5px "Lato", sans-serif; }
  .warning { position: absolute; top: 430px; left: 13px; right: 13px; font: 400 4.2px/1.3 "Lato", sans-serif; text-align: justify; color: var(--body-ink); }
  .warning strong { font-weight: 700; }
  .bottler { position: absolute; top: 478px; left: 18px; font: 400 5px/1.5 "Lato", sans-serif; text-align: left; color: var(--body-ink); text-transform: uppercase; }
  .mini-brand { position: absolute; top: 488px; right: 16px; font: 400 8.5px "Josefin Sans", sans-serif; color: var(--brand); }

  .chai .product-name { color: var(--chai-ink); }
  .chai .tagline, .chai .slogan { color: var(--chai-accent); }
  .chai .photo { background: var(--chai-photo); }
  .chai .volume, .chai .story, .chai .site { color: var(--chai-ink); }

  .mint .product-name { color: var(--mint-ink); }
  .mint .tagline, .mint .slogan { color: var(--mint-accent); }
  .mint .photo { background: var(--mint-photo); }
  .mint .volume, .mint .story { color: var(--mint-accent); }
  .mint .site { color: #ffffff; }

  .pink .product-name { color: var(--pink-ink); }
  .pink .tagline, .pink .slogan { color: var(--pink-accent); }
  .pink .photo { background: var(--pink-photo); }
  .pink .volume, .pink .story { color: var(--pink-accent); }
  .pink .site { color: var(--pink-ink); }
</style>
</head>
<body>
<main class="lineup">

  <article class="bottle chai front" style="left:62px">
    <svg class="silhouette" viewBox="0 0 146 570" width="146" height="570" aria-hidden="true">
      <path d="M48 0H98V140C98 185 146 195 146 245V552Q146 570 128 570H18Q0 570 0 552V245C0 195 48 185 48 140Z" fill="var(--chai-sleeve)"/>
      <rect x="46" y="0" width="54" height="80" rx="4" fill="var(--cap)"/>
      <rect x="47" y="80" width="52" height="11" fill="var(--chai-band)"/>
    </svg>
    <p class="neck-url">www.TovelinSpirits.example</p>
    <div class="sleeve">
      <div class="brand"><span class="brand-dot"></span><span class="brand-name">Tovelin Spirits</span></div>
      <h2 class="product-name">Borvelle</h2>
      <p class="tagline">Black tea, vodka, &amp; aromatic spices</p>
      <div class="photo" role="img" aria-label="Photo of cinnamon sticks, star anise, cardamom and cloves"></div>
      <p class="volume"><span>12% ALC/VOL</span><span>750ml</span></p>
      <p class="slogan">Bring the bartender home</p>
    </div>
  </article>

  <article class="bottle chai back" style="left:223px">
    <svg class="silhouette" viewBox="0 0 146 570" width="146" height="570" aria-hidden="true">
      <path d="M48 0H98V140C98 185 146 195 146 245V552Q146 570 128 570H18Q0 570 0 552V245C0 195 48 185 48 140Z" fill="var(--chai-sleeve)"/>
      <rect x="46" y="0" width="54" height="80" rx="4" fill="var(--cap)"/>
      <rect x="47" y="80" width="52" height="11" fill="var(--chai-band)"/>
    </svg>
    <p class="neck-url">www.TovelinSpirits.example</p>
    <div class="sleeve">
      <div class="brand"><span class="brand-dot"></span><span class="brand-name">Tovelin Spirits</span></div>
      <h2 class="product-name">Borvelle</h2>
      <p class="story">Forget what you think you know about chai, this is not the Queen's tea-time drink! Borvelle is a smooth, sweetly-spiced cocktail made with vodka, black tea, and a combination of aromatic spices. This velvety cocktail is rich without being heavy. Enjoy chilled or over ice anytime.</p>
      <p class="site">www.TovelinSpirits.example</p>
      <p class="warning"><strong>GOVERNMENT WARNING:</strong> (1) ACCORDING TO THE SURGEON GENERAL, WOMEN SHOULD NOT DRINK ALCOHOLIC BEVERAGES DURING PREGNANCY BECAUSE OF THE RISK OF BIRTH DEFECTS. (2) CONSUMPTION OF ALCOHOLIC BEVERAGES IMPAIRS YOUR ABILITY TO DRIVE A CAR OR OPERATE MACHINERY, AND MAY CAUSE HEALTH PROBLEMS.</p>
      <p class="bottler">Bottled by<br>QRW Spirits Company</p>
      <p class="mini-brand">Tovelin</p>
    </div>
  </article>

  <article class="bottle mint front" style="left:424px">
    <svg class="silhouette" viewBox="0 0 146 570" width="146" height="570" aria-hidden="true">
      <path d="M48 0H98V140C98 185 146 195 146 245V552Q146 570 128 570H18Q0 570 0 552V245C0 195 48 185 48 140Z" fill="var(--mint-sleeve)"/>
      <rect x="46" y="0" width="54" height="80" rx="4" fill="var(--cap)"/>
      <rect x="47" y="80" width="52" height="11" fill="var(--mint-band)"/>
    </svg>
    <p class="neck-url">www.TovelinSpirits.example</p>
    <div class="sleeve">
      <div class="brand"><span class="brand-dot"></span><span class="brand-name">Tovelin Spirits</span></div>
      <h2 class="product-name">Faluntera</h2>
      <p class="tagline">Lime, cucumber, mint, spicy pepper &amp; gin</p>
      <div class="photo" role="img" aria-label="Photo of cucumber slices, lime halves and mint leaves"></div>
      <p class="volume"><span>12% ALC/VOL</span><span>750ml</span></p>
      <p class="slogan">Bring the bartender home</p>
    </div>
  </article>

  <article class="bottle mint back" style="left:592px">
    <svg class="silhouette" viewBox="0 0 146 570" width="146" height="570" aria-hidden="true">
      <path d="M48 0H98V140C98 185 146 195 146 245V552Q146 570 128 570H18Q0 570 0 552V245C0 195 48 185 48 140Z" fill="var(--mint-sleeve)"/>
      <rect x="46" y="0" width="54" height="80" rx="4" fill="var(--cap)"/>
      <rect x="47" y="80" width="52" height="11" fill="var(--mint-band)"/>
    </svg>
    <p class="neck-url">www.TovelinSpirits.example</p>
    <div class="sleeve">
      <div class="brand"><span class="brand-dot"></span><span class="brand-name">Tovelin Spirits</span></div>
      <h2 class="product-name">Faluntera</h2>
      <p class="story">Faluntera can't make up its mind! This fusion of lime, sweet mint, earthy cucumber and spicy chilies is so refreshing you'll crave it on a hot summer day or a cool winter's night. The exotic botanicals in gin add a complexity to the cocktail making this a refreshing but potent drink! Enjoy chilled or over ice anytime.</p>
      <p class="site">www.TovelinSpirits.example</p>
      <p class="warning"><strong>GOVERNMENT WARNING:</strong> (1) ACCORDING TO THE SURGEON GENERAL, WOMEN SHOULD NOT DRINK ALCOHOLIC BEVERAGES DURING PREGNANCY BECAUSE OF THE RISK OF BIRTH DEFECTS. (2) CONSUMPTION OF ALCOHOLIC BEVERAGES IMPAIRS YOUR ABILITY TO DRIVE A CAR OR OPERATE MACHINERY, AND MAY CAUSE HEALTH PROBLEMS.</p>
      <p class="bottler">Bottled by<br>QRW Spirits Company</p>
      <p class="mini-brand">Tovelin</p>
    </div>
  </article>

  <article class="bottle pink front" style="left:789px">
    <svg class="silhouette" viewBox="0 0 146 570" width="146" height="570" aria-hidden="true">
      <path d="M48 0H98V140C98 185 146 195 146 245V552Q146 570 128 570H18Q0 570 0 552V245C0 195 48 185 48 140Z" fill="var(--pink-sleeve)"/>
      <rect x="46" y="0" width="54" height="80" rx="4" fill="var(--cap)"/>
      <rect x="47" y="80" width="52" height="11" fill="var(--pink-band)"/>
    </svg>
    <p class="neck-url">www.TovelinSpirits.example</p>
    <div class="sleeve">
      <div class="brand"><span class="brand-dot"></span><span class="brand-name">Tovelin Spirits</span></div>
      <h2 class="product-name">Pomadrine</h2>
      <p class="tagline">Lychee fruit, ginger &amp; whiskey</p>
      <div class="photo" role="img" aria-label="Photo of lychee fruit, peeled and whole, with ginger root"></div>
      <p class="volume"><span>12% ALC/VOL</span><span>750ml</span></p>
      <p class="slogan">Bring the bartender home</p>
    </div>
  </article>

  <article class="bottle pink back" style="left:959px">
    <svg class="silhouette" viewBox="0 0 146 570" width="146" height="570" aria-hidden="true">
      <path d="M48 0H98V140C98 185 146 195 146 245V552Q146 570 128 570H18Q0 570 0 552V245C0 195 48 185 48 140Z" fill="var(--pink-sleeve)"/>
      <rect x="46" y="0" width="54" height="80" rx="4" fill="var(--cap)"/>
      <rect x="47" y="80" width="52" height="11" fill="var(--pink-band)"/>
    </svg>
    <p class="neck-url">www.TovelinSpirits.example</p>
    <div class="sleeve">
      <div class="brand"><span class="brand-dot"></span><span class="brand-name">Tovelin Spirits</span></div>
      <h2 class="product-name">Pomadrine</h2>
      <p class="story">East meet West. Delicate lychee meet hard-hitting whiskey. Pomadrine will tempt your senses with flavor, fragrance and beauty. The peppery kick of ginger and the intensity of the un-aged whiskey are softened by lychee's intoxicating scent and subtle, sweet finish. Enjoy chilled or over ice anytime.</p>
      <p class="site">www.TovelinSpirits.example</p>
      <p class="warning"><strong>GOVERNMENT WARNING:</strong> (1) ACCORDING TO THE SURGEON GENERAL, WOMEN SHOULD NOT DRINK ALCOHOLIC BEVERAGES DURING PREGNANCY BECAUSE OF THE RISK OF BIRTH DEFECTS. (2) CONSUMPTION OF ALCOHOLIC BEVERAGES IMPAIRS YOUR ABILITY TO DRIVE A CAR OR OPERATE MACHINERY, AND MAY CAUSE HEALTH PROBLEMS.</p>
      <p class="bottler">Bottled by<br>QRW Spirits Company</p>
      <p class="mini-brand">Tovelin</p>
    </div>
  </article>

</main>
</body>
</html>
```